EXAMINATION OF OSTEOPOROSIS BONE DENSITOMETRY

I need an illustrative broscure of the service we offer, and inside will be placed the report of the examination performed.
The report is the size of an A4 sheet.
I want people to have in their hands a nice folder where they can read our data and what we do.
So even when they go to their doctor to bring the result of the examination performed, they can see through fraud what we do in our center.

Target Market(s)

THE REFERENCE PLATES ARE people between 35 and 80 years who have problems with osteoporosis and must perform a diagnostic examination "BONE DENSITOMETRY" ARE FRAGILE PEOPLE WITH LITTLE CALCIUM IN THE BONES. The examination is prescribed by both gynecologists and endocrinologists

Industry/Entity Type

diagnostic center

Colors
0054AA
0677BA
7BADD7
CADEEF
E8F1F8
0094D4
00A9DD
6FCCEA
C7EBF8
E9F6FB
00AB8E
00BBA5
67D7C9
C6EFE9
E9F9F6

Requirements
Must have
• my pregetto must have the logo clearly visible "Tavoro Med", then you have to insert the images that I have provided to understand what type of examination it is
Nice to have
• I would like to have a folder that can contain inside the report of the examination performed. the report has the size of an A4 sheet. So you need a folder that opens like a book. Outside must have all images, our logo all the contact details of our center. must be a delicate folder using the colors of our logo, but at the same time must be very incisive to understand what we do

```html
<!DOCTYPE html>
<html lang="it">
<head>
<meta charset="utf-8">
<title>Tavoro Med – Examination Report</title>
<link href="https://fonts.googleapis.com/css2?family=Archivo+Black&family=Arimo:wght@400;700&display=swap" rel="stylesheet">
<style>
  :root{
    --blue:#0677BA;
    --blue-dark:#0054AA;
    --teal:#00AB8E;
    --teal-light:#00BBA5;
    --white:#ffffff;
    --ink:#111111;
    --neutral-light:#f1f2f3;
    --neutral-mid:#d9dcdf;
  }
  html,body{margin:0;padding:0;overflow:hidden;background:#fff;}
  .sheet{width:961px;height:1200px;position:relative;overflow:hidden;background:var(--white);font-family:"Arimo",Arial,sans-serif;}
  .backdrop{position:absolute;left:0;top:0;width:961px;height:1200px;}
  .abs{position:absolute;margin:0;}

  .brand{left:455px;top:44px;}
  .brand-name{display:flex;align-items:center;gap:14px;font-weight:700;font-size:66px;line-height:1;color:var(--blue);letter-spacing:-.5px;}
  .brand-dot{width:19px;height:19px;border-radius:50%;background:var(--teal-light);flex:none;}
  .brand-tagline{margin-top:8px;padding-left:3px;font-size:19px;font-weight:700;color:var(--teal-light);}

  .title{left:60px;top:222px;color:var(--white);}
  .title h1{margin:0;font-family:"Archivo Black",Arial,sans-serif;font-weight:400;font-size:39px;line-height:1;}
  .title p{margin:5px 0 0;font-size:23px;letter-spacing:.3px;line-height:1;}

  .photo{top:313px;width:258px;height:216px;background:linear-gradient(180deg,var(--neutral-light),var(--neutral-mid));}
  .photo-charts{left:60px;}
  .photo-report{left:353px;}
  .photo-scanner{left:646px;}

  .body-text{left:60px;width:844px;color:var(--white);font-size:20.6px;line-height:25.5px;}
  .body-text .line{display:block;text-align:justify;text-align-last:justify;}
  .body-text .line.last{text-align:left;text-align-last:left;}
  .intro{top:552px;}
  .stats{top:680px;}

  .risk-box{left:62px;top:833px;width:462px;height:187px;background:var(--white);box-sizing:border-box;padding:9px 0 0 26px;}
  .risk-box p{margin:0;color:var(--blue);font-size:26.5px;line-height:32.7px;}

  .campaign{left:567px;top:823px;color:var(--white);font-size:23.3px;line-height:29px;}
  .campaign strong{color:var(--teal-light);}
  .cta{left:568px;top:1076px;color:var(--white);font-size:24px;font-weight:700;line-height:1;}

  .contact{display:flex;align-items:center;gap:13px;font-size:18px;color:var(--ink);}
  .contact-icon{width:30px;height:30px;border-radius:50%;background:var(--teal);display:flex;align-items:center;justify-content:center;flex:none;}
  .contact-icon svg{width:16px;height:16px;}
  .addr{left:60px;top:1104px;}
  .row2{top:1144px;}
  .phone{left:60px;}
  .mobile{left:257px;}
  .mail{left:461px;}
  .web{left:704px;}
</style>
</head>
<body>
<div class="sheet">
  <svg class="backdrop" viewBox="0 0 1275 1650" preserveAspectRatio="none" aria-hidden="true">
    <polygon points="0,48 574,48 474,208 0,208" fill="var(--blue)"/>
    <polyline points="0,212 622,212 598,262 1062,262 1036,302" fill="none" stroke="var(--teal-light)" stroke-width="9"/>
    <polygon points="0,218 612,218 588,268 1052,268 1030,303 1275,303 1275,1528 656,1528 680,1478 192,1478 216,1443 0,1443" fill="var(--blue)"/>
    <polyline points="190,1486 676,1486 650,1536 1275,1536" fill="none" stroke="var(--teal-light)" stroke-width="10"/>
    <polygon points="190,1486 222,1443 260,1443 228,1486" fill="var(--teal-light)"/>
  </svg>

  <div class="abs brand">
    <div class="brand-name"><span class="brand-dot"></span>Tavoro Med</div>
    <div class="brand-tagline">Health Care Diagnostic</div>
  </div>

  <div class="abs title">
    <h1>EXAMINATION REPORT</h1>
    <p>OF OSTEOPOROSIS BONE DENSITOMETRY</p>
  </div>

  <div class="abs photo photo-charts" role="img" aria-label="Densitometry scans of spine and hip with bone density reference charts"></div>
  <div class="abs photo photo-report" role="img" aria-label="Sample DXA examination report with spine scan, X-ray and data tables"></div>
  <div class="abs photo photo-scanner" role="img" aria-label="Bone densitometry scanner with examination table"></div>

  <p class="abs body-text intro">
    <span class="line">L'Osteoporosi è una malattia comune che colpisce milioni di donne nel mondo ma,</span>
    <span class="line">purtroppo, ancora oggi sottovalutata.&nbsp; Rende fragili le ossa, che quindi possono</span>
    <span class="line">fratturarsi più facilmente.&nbsp; Fratture che possono essere molto gravi, la più temibile è</span>
    <span class="line last">quella del femore.</span>
  </p>

  <p class="abs body-text stats">
    <span class="line">Solo in Italia, a causa dell'osteoporosi, ogni anno circa 70 mila donne subiscono la</span>
    <span class="line">frattura del femore; il progressivo invecchiamento della popolazione porterà ad un</span>
    <span class="line">aumento drammatico di questo tipo di fratture. Una delle caratteristiche della malattia</span>
    <span class="line">è quella di essere silenziosa fino all'età avanzata, quando si manifesta con:</span>
    <span class="line last">incurvamento della colonna e dolori alla parte bassa della schiena.</span>
  </p>

  <div class="abs risk-box">
    <p>Attenzione: una dieta povera di<br>calcio o ricca di proteine, la<br>mancanza di moto, l'abitudine<br>al fumo e il consumo di alcool<br>sono tutti fattori predisponenti.</p>
  </div>

  <p class="abs campaign">Per rispondere alla poca<br>informazione dei pazienti<br>giunti alle conseguenze più<br>gravi senza coscienza del<br>problema <strong>TAVORO MED</strong><br>promuove una campagna di<br>sensibilizzazione e<br>diagnostica.</p>

  <p class="abs cta">Chiamaci!</p>

  <div class="abs contact addr">
    <span class="contact-icon"><svg viewBox="0 0 24 24"><path d="M12 2a7 7 0 0 0-7 7c0 5 7 13 7 13s7-8 7-13a7 7 0 0 0-7-7zm0 9.5a2.5 2.5 0 1 1 0-5 2.5 2.5 0 0 1 0 5z" fill="#fff"/></svg></span>
    <span>Via dei Tigli, 18&nbsp; 47890 Borgo Sereno (RSM)</span>
  </div>
  <div class="abs contact row2 phone">
    <span class="contact-icon"><svg viewBox="0 0 24 24"><path d="M6.6 10.8a15 15 0 0 0 6.6 6.6l2.2-2.2a1 1 0 0 1 1-.25 11.4 11.4 0 0 0 3.6.57 1 1 0 0 1 1 1V20a1 1 0 0 1-1 1A17 17 0 0 1 3 4a1 1 0 0 1 1-1h3.5a1 1 0 0 1 1 1c0 1.25.2 2.45.57 3.57a1 1 0 0 1-.25 1z" fill="#fff"/></svg></span>
    <span>0549-00 12 34</span>
  </div>
  <div class="abs contact row2 mobile">
    <span class="contact-icon"><svg viewBox="0 0 24 24"><rect x="7" y="2" width="10" height="20" rx="2" fill="#fff"/><rect x="9" y="5" width="6" height="11" fill="var(--teal)"/></svg></span>
    <span>351-00 222 00</span>
  </div>
  <div class="abs contact row2 mail">
    <span class="contact-icon"><svg viewBox="0 0 24 24"><rect x="3" y="6" width="18" height="12" rx="1" fill="#fff"/><path d="M3 6l9 7 9-7" fill="none" stroke="var(--teal)" stroke-width="1.5"/></svg></span>
    <span>info@tavoromed.it</span>
  </div>
  <div class="abs contact row2 web">
    <span class="contact-icon"><svg viewBox="0 0 24 24"><circle cx="12" cy="12" r="9" fill="none" stroke="#fff" stroke-width="2"/><path d="M3 12h18M12 3c3 3 3 15 0 18M12 3c-3 3-3 15 0 18" fill="none" stroke="#fff" stroke-width="1.5"/></svg></span>
    <span>www.tavoromed.it</span>
  </div>
</div>
</body>
</html>
```